Home Staging Company needs business card design

We're a home staging company called Brightwell Harbor Home Staging. We would like a business card design that includes aqua and gray. Our current logo of house within chair is fine but I find we almost always use the logo in one color. I'll upload images of front and back of our current card and our logo. Note that we have dropped "Solutions" from our company name and don't want to include it on the card.

Target Market(s)

Realtors and homeowners - people interested in selling their homes

Contact Information for Business Card

Marisol Fenwickley
Brightwell Harbor Home Staging
757-382-6190
www.brightwellharbor.com
marisol@brightwellharbor.com

Font styles to use
Serif
Script

Requirements
Must have
• My logo and contact details
• UPDATE***
• I forgot to say that the company name should be included on the front of the card somehow.

```html
<!DOCTYPE html>
<html lang="en">
<head>
<meta charset="utf-8">
<title>Brightwell Harbor Home Staging – Business Card</title>
<link href="https://fonts.googleapis.com/css2?family=Tinos:wght@400;700&display=swap" rel="stylesheet">
<style>
  :root{
    --aqua:#38bcc6;
    --charcoal:#454545;
    --ink:#ffffff;
    --stage:#e6e7e8;
  }
  *{box-sizing:border-box;margin:0;padding:0}
  html,body{width:1200px;height:900px;overflow:hidden;background:var(--stage)}
  body{font-family:"Tinos","Times New Roman",serif;position:relative}
  .card{position:absolute;left:250px;width:700px;height:400px;overflow:hidden;box-shadow:0 6px 18px rgba(0,0,0,.18)}
  .card--front{top:40px;background:var(--charcoal)}
  .card--back{top:460px;background:var(--aqua)}
  .card__shapes{position:absolute;inset:0}
  .holder{position:absolute;right:70px;top:62px;text-align:right;color:var(--ink)}
  .holder__name{font-size:32px;font-variant:small-caps;letter-spacing:.5px;line-height:1}
  .holder__role{font-size:13px;margin-top:6px}
  .contact{position:absolute;right:56px;color:var(--ink);font-size:15px}
  .contact--phone{top:158px}
  .contact--email{top:192px}
  .contact__row{display:flex;align-items:center;gap:10px}
  .icon{width:20px;height:20px;flex:none}
  .brand{position:absolute;display:flex;align-items:center;gap:16px}
  .brand__mark{width:64px;height:64px;border-radius:50%;flex:none}
  .brand__name{font-size:28px;line-height:1.15}
  .card--front .brand{left:60px;top:150px}
  .card--front .brand__mark{background:var(--aqua)}
  .card--front .brand__name{color:var(--aqua)}
  .card--back .brand{left:50%;top:110px;transform:translateX(-50%)}
  .card--back .brand__mark{background:var(--ink)}
  .card--back .brand__name{color:var(--ink)}
  .web{position:absolute;color:var(--ink);font-size:17px;display:flex;align-items:center;gap:10px}
  .card--front .web{left:385px;top:292px}
  .card--back .web{left:225px;top:312px}
</style>
</head>
<body>

<section class="card card--front" aria-label="Front of card">
  <svg class="card__shapes" viewBox="0 0 700 400" width="700" height="400" aria-hidden="true">
    <path d="M315,331 C340,331 340,280 365,280 L615,280 C640,280 640,331 665,331 Z" fill="#38bcc6"/>
    <rect x="0" y="330" width="700" height="2" fill="#38bcc6"/>
  </svg>

  <div class="holder">
    <p class="holder__name">Marisol Fenwickley</p>
    <p class="holder__role">Designation</p>
  </div>

  <div class="contact contact--phone contact__row">
    <span>757-382-6190</span>
    <svg class="icon" viewBox="0 0 20 20"><circle cx="10" cy="10" r="9" fill="none" stroke="#38bcc6" stroke-width="1.5"/><path d="M6.5 5.5l2 0 1 2.5-1.3 1a6 6 0 0 0 2.8 2.8l1-1.3 2.5 1v2a1 1 0 0 1-1 1A8 8 0 0 1 5.5 6.5a1 1 0 0 1 1-1z" fill="#38bcc6"/></svg>
  </div>
  <div class="contact contact--email contact__row">
    <span>marisol@brightwellharbor.com</span>
    <svg class="icon" viewBox="0 0 20 20"><circle cx="10" cy="10" r="9" fill="none" stroke="#38bcc6" stroke-width="1.5"/><rect x="5" y="6.5" width="10" height="7" rx="1" fill="#38bcc6"/><path d="M5.5 7l4.5 3.5L14.5 7" fill="none" stroke="#454545" stroke-width="1"/></svg>
  </div>

  <div class="brand">
    <span class="brand__mark" aria-hidden="true"></span>
    <p class="brand__name">Brightwell Harbor<br>Home Staging</p>
  </div>

  <div class="web">
    <svg class="icon" viewBox="0 0 20 20"><circle cx="10" cy="10" r="9" fill="none" stroke="#fff" stroke-width="1.5"/><circle cx="10" cy="10" r="5" fill="none" stroke="#fff" stroke-width="1"/><path d="M5 10h10M10 5v10" stroke="#fff" stroke-width="1"/></svg>
    <span>www.brightwellharbor.com</span>
  </div>
</section>

<section class="card card--back" aria-label="Back of card">
  <svg class="card__shapes" viewBox="0 0 700 400" width="700" height="400" aria-hidden="true">
    <path d="M0,300 L150,300 C175,300 175,348 200,348 L520,348 C545,348 545,300 570,300 L700,300 L700,400 L0,400 Z" fill="#454545"/>
  </svg>

  <div class="brand">
    <span class="brand__mark" aria-hidden="true"></span>
    <p class="brand__name">Brightwell Harbor<br>Home Staging</p>
  </div>

  <div class="web">
    <svg class="icon" viewBox="0 0 20 20"><circle cx="10" cy="10" r="9" fill="none" stroke="#fff" stroke-width="1.5"/><circle cx="10" cy="10" r="5" fill="none" stroke="#fff" stroke-width="1"/><path d="M5 10h10M10 5v10" stroke="#fff" stroke-width="1"/></svg>
    <span>www.brightwellharbor.com</span>
  </div>
</section>

</body>
</html>
```